Rising Paths Web Design

I am starting a new company that will provide LIFE COACHING services - I have tried to design a website, but it's too complicated. Right now, it's just me - I'm the only person that will provide services through the website - I have used artmarket to purchase a logo (see below). I want to be able to update the website myself, but need a template - basic design. Because I am not technologically savvy enough to explain in words - I basically want to have a website that will provide basic information about my services (coaching), a page about me and my background, hopefully scheduling possibilities, and testimonials — also a page for writing/blogs. I bought a website through NetHarbor - so when I have a template, I guess I”d use that - but maybe I’ll need to work with a designer to actually get it up on the internet. I have a head shot that I’ll upload, too.
Target Market(s)
Clients from the independent (private school) world - teachers, administrators
Number of Pages Required
4 page
Look and feel
Each slider illustrates characteristics of the customer's brand and the style your logo design should communicate.

```html
<!DOCTYPE html>
<html lang="en">
<head>
<meta charset="utf-8">
<title>Rising Paths — Life Coaching</title>
<link href="https://fonts.googleapis.com/css2?family=Lora:wght@400;500;600&family=Libre+Baskerville:wght@400;700&family=Roboto:wght@400;500&display=swap" rel="stylesheet">
<style>
:root{
  --teal:#2d8a74;
  --accent:#14a88c;
  --ink:#1f2329;
  --muted:#7a7f86;
  --light:#f2f2f2;
  --footer:#1e222c;
  --footer-deep:#181b23;
  --white:#ffffff;
}
*{margin:0;padding:0;box-sizing:border-box}
html,body{width:1200px;height:3638px;overflow:hidden;background:var(--white)}
body{position:relative;font-family:"Libre Baskerville",Georgia,serif;color:var(--ink)}
.abs{position:absolute}
.serif{font-family:"Lora",Georgia,serif}

/* hero */
.hero{left:0;top:0;width:1200px;height:593px;background:linear-gradient(100deg,#2b2f2f 0%,#4a4a44 40%,#3b3a36 70%,#2a2c2c 100%)}
.hero-shade{left:0;top:0;width:1200px;height:593px;background:linear-gradient(90deg,rgba(0,0,0,.45),rgba(0,0,0,.1))}
.brand{left:88px;top:58px;display:flex;align-items:center;gap:10px;color:var(--white);font-family:"Lora",serif;font-size:13px;letter-spacing:.5px}
.brand-dot{width:26px;height:26px;border-radius:50%;border:2px solid var(--accent)}
.topbar{top:24px;left:700px;display:flex;gap:34px;color:var(--white);font-size:11px;align-items:center}
.topbar span{display:flex;align-items:center;gap:7px}
.socials{display:flex;gap:14px}
.socials i{width:8px;height:8px;border-radius:50%;background:var(--white);display:block}
.nav{top:65px;left:467px;display:flex;gap:41px;color:var(--white);font-size:11px;font-weight:700;letter-spacing:.4px}
.nav-mark{left:302px;top:86px;width:42px;height:2px;background:var(--accent)}
.hero-name{left:86px;top:238px;color:#d6d6d6;font-family:"Lora",serif;font-size:20px}
.hero-title{left:86px;top:280px;color:var(--white);font-family:"Lora",serif;font-size:53px;font-weight:600;line-height:62px}
.btn-solid{left:85px;top:443px;width:138px;height:46px;background:var(--accent);color:var(--white);font-size:11px;font-weight:700;display:flex;align-items:center;justify-content:center;letter-spacing:.3px}
.headshot{left:688px;top:253px;width:326px;height:435px;background:linear-gradient(160deg,#d8d2c4,#bdb29c 55%,#e8e4dc);box-shadow:0 8px 24px rgba(0,0,0,.18)}

/* intro */
.intro-title{left:270px;top:756px;width:640px;font-family:"Lora",serif;font-size:30px;font-weight:500;line-height:41px}
.intro-text{left:270px;top:898px;width:670px;font-size:14px;line-height:20.5px;color:#8c9096}
.btn-line{display:flex;align-items:center;justify-content:center;font-size:11px;font-weight:700;letter-spacing:.3px;border:1.5px solid var(--accent);color:var(--accent)}
.intro-btn{left:270px;top:998px;width:140px;height:47px}

/* services */
.services{left:0;top:1152px;width:1200px;height:703px;background:var(--teal)}
.sec-title{left:0;width:1200px;text-align:center;font-family:"Lora",serif}
.services-title{top:1202px;color:var(--white);font-size:42px}
.rule{width:60px;height:3px;left:570px}
.card{top:1316px;width:232px;height:319px;background:var(--white)}
.card-img{width:232px;height:188px}
.card-label{height:131px;display:flex;align-items:center;justify-content:center;text-align:center;padding:0 26px;font-family:"Lora",serif;font-size:15px;font-weight:500;line-height:23px}
.dots{top:1711px;left:576px;display:flex;gap:8px}
.dots i{width:9px;height:9px;border-radius:50%;border:1.5px solid #1c3a33;display:block}
.dots i.on{background:#1c3a33}
.services-btn{left:529px;top:1745px;width:142px;height:47px;border-color:var(--white);color:var(--white)}

/* events */
.events{left:0;top:1855px;width:1200px;height:715px;background:var(--light)}
.events-title{top:1942px;color:var(--accent);font-size:31px;font-weight:500}
.post{left:62px;width:573px;height:186px;background:var(--white);display:flex}
.post-img{width:257px;height:100%}
.post-body{padding:30px 26px 0}
.post-title{font-family:"Lora",serif;font-size:16.5px;font-weight:500;line-height:25px}
.meta{font-size:9px;color:#555;margin-top:8px}
.meta b{font-weight:400;color:var(--accent)}
.post-text{font-size:12.5px;line-height:22px;color:#666;margin-top:12px}
.link{font-size:10px;color:#999;text-decoration:underline;margin-top:8px;display:block}
.event{left:664px;width:398px;height:117px;background:var(--white);display:flex;align-items:center}
.date{width:120px;text-align:center;color:var(--accent);font-family:"Lora",serif}
.date b{display:block;font-size:38px;font-weight:400;line-height:40px}
.date span{font-size:11px;letter-spacing:3px}
.event-title{font-family:"Lora",serif;font-size:16px;font-weight:500}
.event .meta{margin-top:4px}

/* stories */
.stories-title{top:2672px;font-size:30px;font-weight:500}
.avatar{width:120px;height:120px;border-radius:50%;top:2812px}
.quote{top:2780px;font-family:"Lora",serif;color:var(--accent);font-size:14.5px;display:flex;gap:14px;align-items:center}
.quote b{font-size:22px;font-weight:700;letter-spacing:-2px}
.story-text{top:2815px;width:350px;font-size:13.5px;line-height:26px;color:#333}
.story-name{font-family:"Lora",serif;font-size:13px;font-weight:600;margin-top:12px}
.story-role{font-size:10.5px;color:#aaa;margin-top:4px}
.divider{left:62px;top:3003px;width:1076px;height:1px;background:#ececec}

/* subscribe */
.sub-title{top:3064px;font-size:30px;font-weight:500}
.sub-text{top:3127px;left:300px;width:600px;text-align:center;font-size:12px;line-height:23px;color:#555}
.sub-form{left:339px;top:3205px;width:456px;height:42px;border-radius:21px;background:var(--white);box-shadow:0 6px 18px rgba(0,0,0,.1);display:flex;overflow:hidden}
.sub-input{flex:1;font-family:"Roboto",sans-serif;font-size:11px;color:#444;display:flex;align-items:center;padding-left:21px}
.sub-btn{width:94px;background:var(--accent);color:var(--white);font-family:"Roboto",sans-serif;font-size:10px;font-weight:500;display:flex;align-items:center;justify-content:center}

/* footer */
.footer{left:0;top:3287px;width:1200px;height:307px;background:var(--footer);color:#cfd2d8}
.footer-brand{left:68px;top:3360px;color:var(--white);font-family:"Lora",serif;font-size:14px;display:flex;gap:10px;align-items:center}
.contact-list{left:66px;top:3436px;font-size:11px;line-height:26px}
.contact-list div{display:flex;align-items:center;gap:14px}
.contact-list svg{width:11px;height:11px;fill:#cfd2d8}
.f-socials{left:64px;top:3523px;display:flex;gap:10px}
.f-socials i{width:33px;height:33px;border-radius:50%;border:1px solid #444a56;display:block}
.f-socials i.on{background:var(--accent);border-color:var(--accent)}
.f-col{top:3382px;font-size:11px}
.f-col h4{font-size:11.5px;font-weight:400;color:var(--white);letter-spacing:.2px;margin-bottom:22px}
.f-col p{margin-bottom:16px}
.bottom{left:0;top:3594px;width:1200px;height:44px;background:var(--footer-deep);font-family:"Roboto",sans-serif;font-size:11px;color:#6c7280}
.bottom .copy{position:absolute;left:65px;top:15px}
.bottom .legal{position:absolute;left:840px;top:15px;word-spacing:3px}
</style>
</head>
<body>

<!-- Hero -->
<div class="abs hero" role="img" aria-label="Background photo of a coaching workshop group"></div>
<div class="abs hero-shade"></div>
<div class="abs brand"><span class="brand-dot"></span>RISING PATHS</div>
<div class="abs topbar">
  <span><svg width="10" height="10" viewBox="0 0 24 24" fill="#14a88c"><path d="M6.6 10.8a15 15 0 006.6 6.6l2.2-2.2a1 1 0 011-.25 11.4 11.4 0 003.6.57 1 1 0 011 1V20a1 1 0 01-1 1A17 17 0 013 4a1 1 0 011-1h3.5a1 1 0 011 1 11.4 11.4 0 00.57 3.6 1 1 0 01-.25 1z"/></svg>1 (800) 555-0142</span>
  <span><svg width="11" height="9" viewBox="0 0 24 18" fill="#14a88c"><path d="M0 0h24v18H0z"/></svg>contact@risingpaths.com</span>
  <span class="socials"><i></i><i></i><i></i></span>
</div>
<nav class="abs nav"><span>HOME</span><span>ABOUT ME</span><span>SERVICES</span><span>EVENTS</span><span>TESTIMONIALS</span><span>BLOG</span><span>CONTACT</span></nav>
<div class="abs nav-mark"></div>
<div class="abs hero-name">Clara Whitfield Ames</div>
<h1 class="abs hero-title">Success is a Progressive<br>Idea Worth Pursuing</h1>
<div class="abs btn-solid">BOOK CALL NOW</div>
<div class="abs headshot" role="img" aria-label="Head shot portrait of the coach"></div>

<!-- Intro -->
<h2 class="abs intro-title">I motivate individuals to transform their lives by mindfulness &amp; sharing wisdom for self developement</h2>
<p class="abs intro-text">Lorem ipsum dolor sit amet, consectetur adipiscing elit, sed do eiusmod tempor incididunt ut labore et dolore magna aliqua. Quis ipsum suspendisse ultrices gravida. Risus commodo viverra maecenas accumsan lacus vel facilisis.</p>
<div class="abs btn-line intro-btn">MORE ABOUT ME</div>

<!-- Services -->
<div class="abs services"></div>
<h2 class="abs sec-title services-title">My Services</h2>
<div class="abs rule" style="top:1269px;background:var(--white)"></div>
<div class="abs card" style="left:97px"><div class="card-img" role="img" aria-label="Lecture hall with chalkboards" style="background:linear-gradient(#6b5a3e,#3e3c2e)"></div><div class="card-label">How to become a Biomedical Engineer</div></div>
<div class="abs card" style="left:354px"><div class="card-img" role="img" aria-label="Large seated student audience" style="background:linear-gradient(#c9c2b5,#6d5c52)"></div><div class="card-label">MS in Computer Science Courses in the USA</div></div>
<div class="abs card" style="left:611px"><div class="card-img" role="img" aria-label="Group discussion in a colorful classroom" style="background:linear-gradient(#8a5a4a,#3a3434)"></div><div class="card-label">The study of the human mind.</div></div>
<div class="abs card" style="left:868px"><div class="card-img" role="img" aria-label="Seminar audience in a meeting room" style="background:linear-gradient(#8f8e90,#3e3a44)"></div><div class="card-label">The study of information technology.</div></div>
<div class="abs dots"><i></i><i class="on"></i><i></i></div>
<div class="abs btn-line services-btn">MORE ABOUT ME</div>

<!-- Events & Blogs -->
<div class="abs events"></div>
<h2 class="abs sec-title events-title">Events &amp; Blogs</h2>
<div class="abs rule" style="top:2000px;background:var(--accent)"></div>

<article class="abs post" style="top:2047px">
  <div class="post-img" role="img" aria-label="Classroom wall with colorful value banners" style="background:linear-gradient(120deg,#e9d9a0,#9fc7d8 50%,#d9a3b8)"></div>
  <div class="post-body">
    <h3 class="post-title">Use These Four Guiding Princi-<br>ples in Difficult Conversations</h3>
    <div class="meta">POSTED 08.17.2017 &nbsp;|&nbsp; <b>BY DANA HOLT</b></div>
    <p class="post-text">Don't be distracted by criticism. Remember the only taste of success some people.</p>
  </div>
</article>
<article class="abs post" style="top:2252px">
  <div class="post-img" role="img" aria-label="School fair booths with visitors" style="background:linear-gradient(120deg,#8a8a80,#2f5a4a 70%,#1f3d36)"></div>
  <div class="post-body">
    <h3 class="post-title">Excellent job fair at Kingsford!</h3>
    <div class="meta">POSTED 08.17.2017 &nbsp;|&nbsp; <b>BY DANA HOLT</b></div>
    <p class="post-text">Don't be distracted by criticism. Remember the only taste of success some people.</p>
    <span class="link">VIEW DETAILS</span>
  </div>
</article>

<div class="abs event" style="top:2047px"><div class="date"><b>04</b><span>DEC</span></div><div><div class="event-title">Speaking &amp; Workshops</div><div class="meta">NEWYORK, US &nbsp; 10:00 PM – 06:00 AM</div><span class="link">VIEW DETAILS</span></div></div>
<div class="abs event" style="top:2184px"><div class="date"><b>22</b><span>JUN</span></div><div><div class="event-title">Are You An Effective Leader?</div><div class="meta">NEWYORK, US &nbsp; 10:00 PM – 06:00 AM</div><span class="link">VIEW DETAILS</span></div></div>
<div class="abs event" style="top:2320px"><div class="date"><b>15</b><span>AUG</span></div><div><div class="event-title">Is There an Author Inside You?</div><div class="meta">NEWYORK, US &nbsp; 10:00 PM – 06:00 AM</div><span class="link">VIEW DETAILS</span></div></div>

<!-- Success Stories -->
<h2 class="abs sec-title stories-title">Success Stories</h2>
<div class="abs rule" style="top:2731px;background:var(--accent)"></div>

<div class="abs avatar" style="left:64px;background:linear-gradient(#d9d9d9,#8a7a6e)" role="img" aria-label="Client portrait photo"></div>
<div class="abs quote" style="left:211px"><b>“</b>i have successfully completed</div>
<div class="abs story-text" style="left:213px">Even though I am a seasoned business owner myself, I am sure that there’s always room for growth, inspiration, and new ideas.”
  <div class="story-name">Miles Carter</div><div class="story-role">CEO Fernlight Studio</div></div>

<div class="abs avatar" style="left:579px;background:linear-gradient(#e8e4e2,#7a5a52)" role="img" aria-label="Client portrait photo"></div>
<div class="abs quote" style="left:723px"><b>“</b>i have successfully completed</div>
<div class="abs story-text" style="left:725px">”Coaching has provided a common language that is gaining popularity in the workplace as it creates new learning and sets people up for success. ”
  <div class="story-name">Nora Lindqvist</div><div class="story-role">Creative Director</div></div>

<div class="abs divider"></div>

<!-- Subscribe -->
<h2 class="abs sec-title sub-title">Subscribe Email</h2>
<p class="abs sub-text">Subscribe now and receive weekly newsletter with Coaching materials, new courses, interesting posts, popular books and much more!</p>
<div class="abs sub-form"><div class="sub-input">Enter your email</div><div class="sub-btn">SUBSCRIBE</div></div>

<!-- Footer -->
<footer class="abs footer"></footer>
<div class="abs footer-brand"><span class="brand-dot"></span>RISING PATHS</div>
<div class="abs contact-list">
  <div><svg viewBox="0 0 24 24"><path d="M6.6 10.8a15 15 0 006.6 6.6l2.2-2.2a1 1 0 011-.25 11.4 11.4 0 003.6.57 1 1 0 011 1V20a1 1 0 01-1 1A17 17 0 013 4a1 1 0 011-1h3.5a1 1 0 011 1 11.4 11.4 0 00.57 3.6 1 1 0 01-.25 1z"/></svg>+1 800 555 0199</div>
  <div><svg viewBox="0 0 24 18"><path d="M0 0h24v18H0z"/></svg>info@risingpaths.com</div>
  <div><svg viewBox="0 0 24 24"><path d="M12 2a7 7 0 00-7 7c0 5 7 13 7 13s7-8 7-13a7 7 0 00-7-7zm0 9.5A2.5 2.5 0 1112 6.5a2.5 2.5 0 010 5z"/></svg>12 Orchard Lane 4B, Hudson City, US</div>
</div>
<div class="abs f-socials"><i></i><i class="on"></i><i></i><i></i></div>

<div class="abs f-col" style="left:406px"><h4>FEATURED COURSES</h4><p>Starting Soon</p><p>Just Added</p><p>Most Viewed</p><p>Top Paid</p></div>
<div class="abs f-col" style="left:578px"><h4>CATEGORIES</h4><p>Arts &amp; Design</p><p>Business</p><p>Computer Science</p><p>Data Science</p></div>
<div class="abs f-col" style="left:749px"><h4>USEFUL LINKS</h4><p style="margin-top:-8px">Home</p><p>About Me</p><p>Services</p><p>Testimonial</p></div>
<div class="abs f-col" style="left:895px;top:3405px"><p>Contact</p><p style="margin-top:24px">Blog</p></div>

<div class="abs bottom"><span class="copy">© 2022 Rising Paths. All rights reserved.</span><span class="legal">Privacy | Terms | Sitemap | Help</span></div>

</body>
</html>
```